COMMERCIAL OFFICE FOR SALE- Brochure, Miami, FL 33131

BROCHURE DESIGN BRIEF – COMMERCIAL OFFICE FOR SALE

I need a clean, modern brochure for a commercial office listing (FOR SALE, not lease). This will be used both digitally (email + PlotHarbor/attachments) and printed if needed.

Please follow a “Sample Flyer Copy” style layout — strong headline, clean sections, minimal clutter, and easy to scan. Use fints Seasons and Poppins interchangeably.

All property details, specs, and exact wording should be pulled directly from the MLS Listing file I provided. Do not guess or rewrite specs.

OVERALL LOOK + FEEL

Clean, high-end, professional (Brickell / financial district vibe)

Think: simple, sharp, not busy

Neutral palette (white, black, soft gray) + subtle accent color if needed

Prioritize readability over design gimmicks

Plenty of white space

FORMAT

1-page flyer (primary)

Also format so it can easily convert into a 2-page version if needed

PDF optimized for email + print

HEADER SECTION (TOP OF PAGE)

Large, strong headline:

Example: “Office Condo for Sale | Brickell” (adjust based on MLS info)

Subheadline (smaller):

Key positioning (corner unit, square footage, etc.)

Include 1 strong hero image (best photo of the unit)

PROPERTY OVERVIEW (RIGHT UNDER HEADER OR NEXT BLOCK)

Clean bullet section with icons if possible:

Include:

Total square footage

Layout highlights (conference room, offices, open workspace, etc.)

Kitchen / breakroom

Reception area

Storage / printer room

Floor or suite number

Any standout feature (corner unit, natural light, views, etc.)

Keep this tight and clean — no long paragraphs.

PRICING SECTION

Clearly state: FOR SALE

Price (from MLS)

Price per square foot

Make this visually stand out.

LOCATION SECTION

Short and clean:

Building name + address

1–2 lines max on location advantages (Brickell, access, etc.)

Optional small map if it fits cleanly

ADDITIONAL DETAILS (IF SPACE ALLOWS)

Building amenities (if relevant)

Parking info

Zoning / permitted uses (if applicable)

Only include what is confirmed in MLS.

IMAGES

3–5 total max

Keep it clean — do not overcrowd

Prioritize:

Main workspace

Conference room

Kitchen

Any standout feature

CONTACT SECTION (VERY IMPORTANT – EXACT FORMAT)

This must be clean and prominent.

Delia Moncrief
REALTOR®
Tallowbrook Keystead Partners QNV Realty

Phone: [your number]
Email: [your email]

Call to action line:

“For more information or to schedule a private showing, contact Delia Moncrief.”

Include my business card details (office location etc.) in this section.

BROKERAGE + LOGOS

Use TKP QNV Realty logos provided

Place cleanly (bottom or footer)

Do not distort or restyle logos

FOOTER

Standard disclaimer if needed

Keep minimal

IMPORTANT NOTES

This is a SALE listing — do not use the word lease anywhere

Do not overdesign — clean always wins

Keep everything aligned and balanced

Make sure spacing feels high-end, not cramped
Updates

Please include this video link within the document: https://vidloom.example/tour/Kp7Qz2xLm9?ref=aB3cD4eF5gH6

State: Step inside. Watch the full video tour. and hyperlink Watch with the link

Target Market(s)

Buyers, Professionals, Lawyer Office, Family Office, Small FInancial Offices

Industry/Entity Type

Commercial Real Estate

Font styles to use
Serif
Sans Serif

Requirements
Must have
• Clean, clear, layout and good imagery
Should not have
• Professional flow, follow my font guidlines and thebrochure i shared as a guide

```html
<!DOCTYPE html>
<html lang="en">
<head>
<meta charset="utf-8">
<title>Office Condo for Sale | Brickell</title>
<link rel="stylesheet" href="https://fonts.googleapis.com/css2?family=Poppins:wght@400;500;600;700&display=swap">
<style>
:root{
  --navy:#13304f;
  --ink:#1c2f4a;
  --muted:#5d6670;
  --panel:#f0efee;
  --band:#e8e7e6;
  --rule:#c9c9c9;
  --white:#ffffff;
  --sky:#9bbfd8;
  --wall:#e9e3da;
  --carpet:#8f939a;
}
*{box-sizing:border-box;margin:0;padding:0}
html,body{width:927px;height:1200px;overflow:hidden;background:var(--white)}
body{font-family:"Poppins",sans-serif;color:var(--ink);position:relative}
.abs{position:absolute}
.headline{top:22px;left:0;width:927px;text-align:center;font-size:45px;font-weight:400;color:var(--navy);letter-spacing:-.3px;line-height:1.1}
.headline strong{font-weight:700}
.subhead{top:80px;left:0;width:927px;text-align:center;font-size:18px;color:var(--navy)}
.subhead-rule{top:94px;height:2px;width:124px;background:var(--rule)}
.hero{top:118px;left:0;width:927px;height:313px;background:linear-gradient(180deg,var(--sky) 0%,#cfd9df 38%,var(--wall) 55%,#d8d0c4 80%,var(--carpet) 100%)}
.tagline{top:455px;left:0;width:927px;text-align:center;font-size:13.5px;color:var(--muted)}
.overview{top:492px;left:55px;width:266px;height:361px;background:var(--panel)}
.overview-head{height:34px;background:var(--navy);color:var(--white);font-weight:700;font-size:16px;text-align:center;line-height:34px;letter-spacing:.2px}
.overview-list{list-style:none;padding:6px 25px 0 10px}
.overview-list li{display:flex;align-items:center;height:39.5px;border-bottom:1.5px solid var(--rule);font-size:14.5px;color:var(--navy);white-space:nowrap}
.overview-list li:last-child{border-bottom:none}
.overview-list svg{width:22px;height:22px;margin:0 16px 0 5px;flex:none}
.overview-list b{font-weight:600;margin-right:4px}
.sale-box{top:494px;left:342px;width:523px;height:123px;border:2px solid var(--navy);background:var(--panel)}
.sale-tab{top:-2px;left:176px;width:170px;height:38px}
.sale-tab-label{top:0;left:176px;width:170px;text-align:center;line-height:36px;color:var(--white);font-weight:700;font-size:21px}
.price{top:54px;left:18px;font-size:36px;font-weight:700;color:var(--navy)}
.ppsf{top:60px;right:26px;font-size:21px;font-weight:500;color:var(--navy)}
.ppsf span{font-size:17px}
.info{top:636px;left:342px;width:523px;height:219px;background:var(--panel)}
.info-col{top:14px}
.info h2{font-size:19px;font-weight:600;color:var(--navy);padding:0 0 6px 7px;border-bottom:1.5px solid var(--rule);letter-spacing:.2px;white-space:nowrap}
.info ul{list-style:none;margin-top:12px}
.info li{position:relative;padding-left:24px;font-size:13px;line-height:16.5px;color:var(--navy);margin-bottom:12px}
.info li::before{content:"";position:absolute;left:8px;top:5px;width:7px;height:7px;border-radius:50%;background:var(--navy)}
.details li{margin-bottom:11px}
.info-divider{top:28px;left:256px;width:1.5px;height:176px;background:var(--rule)}
.video-line{top:875px;left:0;width:927px;text-align:center;font-size:19px;color:var(--muted)}
.video-line a{color:var(--navy);font-weight:700;text-decoration:none}
.video-line svg{vertical-align:-3px}
.gallery-item{top:915px;height:121px}
.map{left:0;width:275px;background:linear-gradient(135deg,#e9e6ef,#dcdfe9)}
.shot-a{left:281px;width:211px;background:linear-gradient(180deg,#f2f1ee 0%,#e4e1db 55%,#7f8288 100%)}
.shot-b{left:502px;width:211px;background:linear-gradient(180deg,#f1f0ec 0%,#e2ddd4 55%,#8a8d92 100%)}
.shot-c{left:723px;width:204px;background:linear-gradient(180deg,#eeeae4 0%,#e3ddd5 60%,#7b7e84 100%)}
.contact{top:1036px;left:0;width:927px;height:136px;background:var(--band)}
.headshot{top:-14px;left:15px;width:130px;height:150px;background:linear-gradient(180deg,#d8d5d2,#2d3542)}
.agent-name{top:34px;left:179px;font-size:20px;font-weight:700;color:var(--navy)}
.agent-title{top:60px;left:179px;font-size:14px;color:var(--navy)}
.agent-firm{top:85px;left:180px;font-size:12px;color:var(--navy)}
.agent-contact{top:108px;left:174px;font-size:12px;color:var(--navy);display:flex;gap:16px;align-items:center}
.agent-contact span{display:flex;align-items:center;gap:8px}
.brand{top:40px;left:575px;width:290px;display:flex;align-items:center;gap:12px;font-size:28px;font-weight:700;color:#111}
.brand i{width:14px;height:14px;background:#111;display:block}
.footer{top:1172px;left:0;width:927px;height:28px;background:var(--navy);color:var(--white)}
.cta{top:5px;left:39px;font-size:12px;font-weight:600}
.disclaimer{top:8px;left:592px;font-size:9px;font-weight:500}
.code{top:10px;left:897px;font-size:7px}
</style>
</head>
<body>

<h1 class="abs headline">Office Condo for <strong>SALE | BRICKELL</strong></h1>
<div class="abs subhead-rule" style="left:108px"></div>
<p class="abs subhead">1450 Meridian Ave # 505-B MIAMI, FL 33131-3210</p>
<div class="abs subhead-rule" style="left:704px"></div>

<div class="abs hero" role="img" aria-label="Corner private office with L-shaped desk and floor-to-ceiling windows overlooking Brickell towers"></div>

<p class="abs tagline">Move-in ready 2,146 SF office suite in the heart of Brickell with efficient layout and strong professional presence.</p>

<section class="abs overview">
  <div class="overview-head">PROPERTY OVERVIEW</div>
  <ul class="overview-list">
    <li><svg viewBox="0 0 24 24" fill="none" stroke="#13304f" stroke-width="1.6"><rect x="4" y="6" width="9" height="16"/><rect x="13" y="2" width="7" height="20"/><path d="M7 10h3M7 14h3M7 18h3M16 6h1M16 10h1M16 14h1"/></svg><span><b>2,146</b> SF Office Suite</span></li>
    <li><svg viewBox="0 0 24 24" fill="#13304f"><rect x="2" y="3" width="9" height="18"/><rect x="13" y="3" width="9" height="18"/></svg><span><b>4 Private Offices</b></span></li>
    <li><svg viewBox="0 0 24 24" fill="#13304f"><circle cx="6" cy="7" r="2.5"/><circle cx="12" cy="6" r="2.5"/><circle cx="18" cy="7" r="2.5"/><rect x="3" y="12" width="18" height="3"/><rect x="5" y="16" width="2" height="5"/><rect x="17" y="16" width="2" height="5"/></svg><span>Conference Room</span></li>
    <li><svg viewBox="0 0 24 24" fill="#13304f"><circle cx="7" cy="5" r="2.5"/><rect x="4" y="9" width="6" height="5"/><rect x="2" y="15" width="20" height="3"/><rect x="13" y="11" width="8" height="3"/><rect x="2" y="20" width="20" height="2"/></svg><span>Reception Area</span></li>
    <li><svg viewBox="0 0 24 24" fill="#13304f"><rect x="7" y="3" width="10" height="5"/><rect x="3" y="9" width="18" height="9" rx="2"/><rect x="7" y="15" width="10" height="6" fill="#f0efee" stroke="#13304f" stroke-width="1.5"/></svg><span>Printer / Copy Room</span></li>
    <li><svg viewBox="0 0 24 24" fill="none" stroke="#13304f" stroke-width="1.6"><rect x="3" y="10" width="18" height="11"/><path d="M3 15h18M12 10v11M6 4v4M10 4v4M15 3h4v5h-4z"/></svg><span>Kitchenette / Break Area</span></li>
    <li><svg viewBox="0 0 24 24" fill="#13304f"><path d="M12 2a7 7 0 0 0-7 7c0 5 7 13 7 13s7-8 7-13a7 7 0 0 0-7-7zm0 9.5A2.5 2.5 0 1 1 12 6.5a2.5 2.5 0 0 1 0 5z"/></svg><span>Corner Unit Location</span></li>
    <li><svg viewBox="0 0 24 24" fill="none" stroke="#13304f" stroke-width="1.6"><circle cx="12" cy="12" r="6"/><circle cx="12" cy="12" r="2.5" fill="#13304f"/><path d="M12 2v4M12 18v4M2 12h4M18 12h4M5 5l2.5 2.5M16.5 16.5L19 19M19 5l-2.5 2.5M7.5 16.5L5 19"/></svg><span>Central Business District</span></li>
  </ul>
</section>

<section class="abs sale-box">
  <svg class="abs sale-tab" viewBox="0 0 170 38"><polygon points="0,0 170,0 155,38 15,38" fill="#13304f"/></svg>
  <div class="abs sale-tab-label">FOR SALE</div>
  <div class="abs price">$1,025,000</div>
  <div class="abs ppsf">$477 / <span>Square Feet</span></div>
</section>

<section class="abs info">
  <div class="abs info-col location" style="left:19px;width:226px">
    <h2 style="width:176px">LOCATION</h2>
    <ul>
      <li>1450 Meridian Avenue, Suite 505-B Miami, FL 33131</li>
      <li>Prime Brickell Avenue &amp; Coral Way Location</li>
      <li>Steps to Harbor Row Village &amp; Bayline City Centre</li>
    </ul>
  </div>
  <div class="abs info-divider"></div>
  <div class="abs info-col details" style="left:285px;width:225px">
    <h2>ADDITIONAL DETAILS</h2>
    <ul>
      <li>Covered &amp; Guest Parking</li>
      <li>On-Site Security Guard</li>
      <li>Central A/C &amp; Sprinklers</li>
      <li>Zoning: 6407 | Built 1982</li>
      <li>Last Use: Corporate Office</li>
    </ul>
  </div>
</section>

<p class="abs video-line">Step inside. Watch the full video tour. <a href="https://vidloom.example/tour/Kp7Qz2xLm9?ref=aB3cD4eF5gH6">Watch<svg width="22" height="18" viewBox="0 0 22 18" fill="none" stroke="#13304f" stroke-width="2.4"><path d="M1 9h18M12 2l7 7-7 7"/></svg></a></p>

<div class="abs gallery-item map" role="img" aria-label="Street map of Brickell showing the suite location near SE 12th St"></div>
<div class="abs gallery-item shot-a" role="img" aria-label="Open workspace with kitchenette"></div>
<div class="abs gallery-item shot-b" role="img" aria-label="Reception area with wood reception desk"></div>
<div class="abs gallery-item shot-c" role="img" aria-label="Private office with window views"></div>

<section class="abs contact">
  <div class="abs headshot" role="img" aria-label="Portrait of the listing agent"></div>
  <div class="abs agent-name">Delia Moncrief</div>
  <div class="abs agent-title">REALTOR®</div>
  <div class="abs agent-firm">Tallowbrook Keystead Partners QNV Realty</div>
  <div class="abs agent-contact">
    <span><svg width="16" height="16" viewBox="0 0 24 24"><circle cx="12" cy="12" r="12" fill="#13304f"/><path d="M8 6l2 3-1.3 1.3a8 8 0 0 0 5 5L15 14l3 2-1 2.5c-5 .5-11-5.5-10.5-10.5z" fill="#fff"/></svg>(555) 014-2738</span>
    <span><svg width="16" height="16" viewBox="0 0 24 24"><circle cx="12" cy="12" r="12" fill="#13304f"/><rect x="6" y="8" width="12" height="8" fill="none" stroke="#fff" stroke-width="1.5"/><path d="M6 8l6 5 6-5" fill="none" stroke="#fff" stroke-width="1.5"/></svg>deliamoncrief@mailbox.example</span>
  </div>
  <div class="abs brand"><i></i>TKP QNV Realty</div>
</section>

<footer class="abs footer">
  <div class="abs cta">For more information or to schedule a private showing, contact Delia Moncrief.</div>
  <div class="abs disclaimer">Information is believed to be accurate but not guaranteed.</div>
  <div class="abs code">C67</div>
</footer>

</body>
</html>
```